Hip surgeon needs a educative book cover design

I need to re-design my old book cover for its 3rd edition.
It's a small book dedicated to my patients, who underwent total hip replacement. It's meant to help people getting around the basic care after a total hip replacement surgery and getting back to their normal, active life.
The title is: "Bright mornings: a walking companion guide".
I already had a new logo, new stationery and new website design from PixelHarbor (please see the attachments).
The final design should be look alike the other fresh new designs. It must communicate health, peacefulness.
I also attached the manual as it looks today for reference.
A5 size.
Just cover and back cover.

```html
<!DOCTYPE html>
<html lang="en">
<head>
<meta charset="utf-8">
<title>Bright Mornings – Book Cover, 3rd Edition</title>
<link href="https://fonts.googleapis.com/css2?family=Montserrat:wght@400;700&family=Open+Sans:wght@400&display=swap" rel="stylesheet">
<style>
  :root {
    --blue-deep: #2262a6;
    --blue-title: #1f5c9e;
    --blue-bright: #1f80c8;
    --blue-stripe: #2f8fd6;
    --ink: #3a3a3a;
    --white: #ffffff;
  }
  html, body { margin: 0; padding: 0; overflow: hidden; }
  body { width: 1200px; height: 818px; background: var(--white); }
  .cover {
    position: relative; width: 1200px; height: 818px; overflow: hidden;
    background: var(--white); font-family: "Open Sans", Arial, sans-serif;
  }
  .base-band {
    position: absolute; left: 0; top: 530px; width: 1200px; height: 288px;
    background: var(--blue-deep); border-top: 6px solid var(--blue-stripe);
  }
  .faint-ring { position: absolute; left: 18px; top: 560px; }

  /* back cover */
  .author-photo {
    position: absolute; left: 52px; top: 46px; width: 97px; height: 136px;
    background: linear-gradient(160deg, #d9d4cc, #9a8f86 55%, #e9e7e4);
    box-shadow: 0 0 3px rgba(0,0,0,.35);
  }
  .brand { position: absolute; display: flex; align-items: center; gap: 8px;
    font-family: "Montserrat", Arial, sans-serif; font-weight: 700; white-space: nowrap; }
  .brand .dot { border-radius: 50%; flex: none; }
  .brand--back { left: 172px; top: 42px; font-size: 18px; color: var(--blue-bright); }
  .brand--back .dot { width: 36px; height: 36px; background: var(--blue-bright); }
  .author-bio {
    position: absolute; left: 172px; top: 108px; width: 347px;
    font-size: 11.4px; line-height: 16.3px; color: var(--ink); text-align: justify;
  }
  .author-bio p { margin: 0 0 8px; }
  .isbn-box { position: absolute; left: 48px; top: 651px; width: 189px; height: 66px; background: var(--white); }
  .web-address { position: absolute; left: 48px; top: 728px; font-size: 15.5px; color: var(--white); }

  /* spine */
  .spine-edition {
    position: absolute; left: 590px; top: 0; width: 20px; height: 126px;
    background: var(--blue-bright); color: var(--white);
    writing-mode: vertical-rl; font-family: "Montserrat", Arial, sans-serif;
    font-size: 12px; display: flex; align-items: center; justify-content: center; padding-top: 6px; box-sizing: border-box;
  }
  .spine-title {
    position: absolute; left: 589px; top: 146px; writing-mode: vertical-rl;
    font-family: "Montserrat", Arial, sans-serif; font-size: 14px; color: var(--blue-title); white-space: nowrap;
  }
  .spine-title strong { font-weight: 700; margin-bottom: 6px; }
  .spine-title span { font-weight: 400; color: var(--blue-bright); }
  .brand--spine { left: 588px; top: 612px; writing-mode: vertical-rl; font-size: 13px; gap: 6px; color: var(--white); }
  .brand--spine .dot { width: 24px; height: 24px; background: var(--white); }

  /* front cover */
  .edition-tag {
    position: absolute; left: 624px; top: 37px; width: 178px; height: 30px;
    background: var(--blue-bright); color: var(--white);
    font-family: "Montserrat", Arial, sans-serif; font-size: 17px; letter-spacing: 1px;
    display: flex; align-items: center; justify-content: flex-end; padding-right: 10px; box-sizing: border-box;
  }
  .book-title {
    position: absolute; right: 62px; top: 100px; margin: 0; text-align: right;
    font-family: "Montserrat", Arial, sans-serif; font-weight: 700; font-size: 60px; line-height: 70px;
    color: var(--blue-title); letter-spacing: 1px;
  }
  .book-subtitle {
    position: absolute; right: 62px; top: 232px; margin: 0;
    font-family: "Montserrat", Arial, sans-serif; font-weight: 400; font-size: 24px; color: var(--blue-bright);
  }
  .walking-couple {
    position: absolute; left: 780px; top: 312px; width: 250px; height: 420px;
    border-radius: 110px 110px 40px 40px;
    background: linear-gradient(180deg, #2b7fcb 0%, #2a78c0 52%, #235ea2 60%, rgba(34,98,166,0) 100%);
  }
  .brand--front { left: 690px; top: 720px; font-size: 18px; color: var(--white); }
  .brand--front .dot { width: 42px; height: 42px; background: var(--white); }
</style>
</head>
<body>
<main class="cover">
  <div class="base-band"></div>
  <svg class="faint-ring" width="300" height="300" viewBox="0 0 300 300" aria-hidden="true">
    <circle cx="150" cy="150" r="128" fill="none" stroke="#3570b0" stroke-width="26" opacity=".5"/>
  </svg>

  <section class="back-cover">
    <div class="author-photo" role="img" aria-label="Portrait photo of the author in a white coat"></div>
    <div class="brand brand--back"><span class="dot"></span>Dr. Marcos L. Ferreira</div>
    <div class="author-bio">
      <p>Physician trained UFSL - Federal University of Serra Leste, specialist in Orthopedics and Traumatology with improvement in Hip Surgery in Brazil and abroad, Titular Member SBOR - Brazilian Society of Orthopaedic Rehabilitation, Titular Member of the SBAQ - Brazilian Association of Hip Care, Member the ACJS - American College of Joint Surgeons.</p>
      <p>Secretary of SBAQ / PR, Commissioner of Education and Training SBOR / PR, Full Member of the Technical Chamber of Orthopaedics, CRL / PR. currently exercises its functions in Curitiba / PR, with special interest in hip arthroplasty (prostheses), Arthroscopic Hip Surgery (Video by surgery, minimally invasive) and Trauma of Pelvis and Acetabulum.</p>
    </div>
    <div class="isbn-box"></div>
    <div class="web-address">www.passoleveclinica.com.br</div>
  </section>

  <section class="spine">
    <div class="spine-edition">3rd Edition</div>
    <div class="spine-title"><strong>BRIGHT MORNINGS</strong> <span>A Walking Companion Guide</span></div>
    <div class="brand brand--spine"><span class="dot"></span>Dr. Marcos L. Ferreira</div>
  </section>

  <section class="front-cover">
    <div class="edition-tag">3rd Edition</div>
    <h1 class="book-title">BRIGHT<br>MORNINGS</h1>
    <p class="book-subtitle">A Walking Companion Guide</p>
    <div class="walking-couple" role="img" aria-label="Blue silhouette of an elderly couple walking hand in hand, the man with a cane, reflected below"></div>
    <div class="brand brand--front"><span class="dot"></span>Dr. Marcos L. Ferreira</div>
  </section>
</main>
</body>
</html>
```